Commercial and Multifamily informational website

We need a website for our commercial real estate management company. We will manage offices, retail, apartments and others. Here is the brief verbiage: Providing quality commercial and multifamily portfolio management to Landlords, REITs, and financial institutions. 

Industry/Entity Type

Real Estate

Number of Pages Required

2 page

Font styles to use
Sans Serif
Other font styles liked:
• Muli, Garamond

Colors
0555a3
5c5c5c
3176b5
85acd3
474747

Requirements
Must have
• Home page and contact page

```html
<!DOCTYPE html>
<html lang="en">
<head>
<meta charset="utf-8">
<title>Harlow Real Estate Management</title>
<link rel="stylesheet" href="https://fonts.googleapis.com/css2?family=Open+Sans:wght@600;700&family=Lato:wght@400;700&display=swap">
<style>
  :root {
    --blue: #0a3b85;
    --blue-bright: #0555a3;
    --ink: #474747;
    --grey: #5c5c5c;
    --light: #f0f0f0;
    --line: #9aa6b8;
    --dark: #252525;
    --dark-card: #3a3a3a;
    --white: #ffffff;
    --head: "Open Sans", sans-serif;
    --body: "Lato", sans-serif;
  }
  * { box-sizing: border-box; margin: 0; padding: 0; }
  html, body { width: 802px; height: 1200px; overflow: hidden; background: var(--white); }
  body { position: relative; font-family: var(--body); color: var(--ink); }
  .abs { position: absolute; }

  /* header */
  .site-header { position: absolute; left: 0; top: 0; width: 802px; height: 61px; background: var(--white); }
  .brand { position: absolute; left: 54px; top: 15px; display: flex; align-items: center; gap: 6px; }
  .brand-name { font-family: var(--head); font-weight: 700; font-size: 20px; color: var(--blue); letter-spacing: 1px; }
  .brand-sub { font-family: var(--head); font-weight: 600; font-size: 8px; line-height: 8px; color: var(--blue); border-left: 1px solid var(--blue); padding-left: 4px; }
  .main-nav a { position: absolute; top: 24px; font-family: var(--head); font-weight: 600; font-size: 11.5px; color: var(--grey); text-decoration: none; }
  .main-nav a.active { color: var(--blue); }
  .call { position: absolute; left: 643px; top: 15px; display: flex; gap: 6px; align-items: center; }
  .call-text { border-left: 1px solid var(--blue); padding-left: 6px; font-family: var(--head); font-weight: 700; font-size: 9.5px; line-height: 13px; }
  .call-text .label { color: var(--blue); }
  .call-text .num { color: #222; }

  /* hero */
  .hero { position: absolute; left: 0; top: 61px; width: 802px; height: 302px;
    background: linear-gradient(180deg, #2a3f84 0%, #3a5aa6 45%, #27407a 75%, #1c2a4e 100%); }
  .hero-title { position: absolute; left: 0; top: 102px; width: 802px; text-align: center; font-family: var(--head); font-weight: 700; font-size: 15px; line-height: 22px; color: var(--white); }
  .hero-btn { position: absolute; left: 344px; top: 159px; width: 114px; height: 31px; border: 2px solid var(--white); color: var(--white); font-family: var(--head); font-weight: 700; font-size: 11px; display: flex; align-items: center; justify-content: center; }
  .hero-arrow { position: absolute; top: 138px; }

  /* welcome */
  .welcome-title { position: absolute; left: 250px; top: 386px; width: 302px; text-align: center; font-family: var(--head); font-weight: 700; font-size: 22px; color: var(--ink); }
  .welcome-title .brand-inline { color: var(--blue); }
  .rule { position: absolute; height: 1px; background: var(--line); }
  .lead { position: absolute; left: 40px; top: 444px; width: 722px; text-align: center; font-weight: 700; font-size: 12px; color: #333; }
  .intro { position: absolute; left: 60px; top: 470px; width: 682px; text-align: center; font-size: 9.3px; line-height: 15.3px; color: var(--grey); }
  .outline-btn { position: absolute; left: 356px; top: 554px; width: 90px; height: 31px; border: 2px solid var(--blue); display: flex; align-items: center; justify-content: center; font-family: var(--head); font-weight: 700; font-size: 11px; color: #222; }

  /* services */
  .services { position: absolute; left: 0; top: 616px; width: 802px; height: 346px; background: var(--light); }
  .services-title { position: absolute; left: 0; top: 24px; width: 802px; text-align: center; font-family: var(--head); font-weight: 700; font-size: 24px; color: var(--ink); }
  .services-title span { color: var(--blue); }
  .card { position: absolute; top: 82px; width: 164px; height: 218px; background: var(--white); border: 1px solid #bdbdbd; }
  .card-photo { position: absolute; left: -1px; top: -1px; width: 164px; height: 106px; }
  .card-icon { position: absolute; left: 64px; top: 89px; width: 34px; height: 34px; border-radius: 50%; background: var(--dark-card); display: flex; align-items: center; justify-content: center; }
  .card.featured .card-icon { background: var(--blue); }
  .card-title { position: absolute; left: 0; top: 128px; width: 162px; text-align: center; font-family: var(--head); font-weight: 700; font-size: 12px; color: var(--ink); }
  .card.featured .card-title { color: var(--blue); }
  .card-text { position: absolute; left: 6px; top: 148px; width: 150px; text-align: center; font-size: 8.6px; line-height: 11.8px; color: var(--ink); }
  .card-btn { position: absolute; left: 45px; top: 206px; width: 72px; height: 24px; background: var(--dark-card); color: var(--white); font-family: var(--head); font-weight: 700; font-size: 8.5px; display: flex; align-items: center; justify-content: center; }
  .card.featured .card-btn { background: var(--blue); }

  /* footer */
  .site-footer { position: absolute; left: 0; top: 962px; width: 802px; height: 205px; background: var(--dark); color: var(--white); }
  .foot-title { position: absolute; top: 28px; font-family: var(--body); font-weight: 700; font-size: 12px; }
  .foot-rule { position: absolute; top: 51px; height: 1px; background: #555; }
  .foot-rule::before { content: ""; position: absolute; left: 0; top: -1px; width: 20px; height: 2px; background: var(--white); }
  .links { position: absolute; left: 54px; top: 62px; list-style: none; font-size: 9px; }
  .links li { height: 24.5px; }
  .links li::before { content: "• "; }
  .contact-block { position: absolute; left: 188px; top: 62px; font-size: 9px; line-height: 14.5px; }
  .contact-block strong { font-weight: 700; }
  .contact-row { position: absolute; left: 186px; display: flex; align-items: center; gap: 8px; font-size: 9px; }
  .field { position: absolute; left: 398px; width: 178px; border: 1px solid #666; background: #1c1c1c; font-weight: 700; font-size: 8.5px; padding: 5px 8px; }
  .submit { position: absolute; left: 398px; top: 153px; width: 71px; height: 22px; background: var(--blue); font-family: var(--head); font-weight: 700; font-size: 8.5px; display: flex; align-items: center; justify-content: center; }
  .divider-v { position: absolute; top: 40px; width: 1px; height: 135px; background: #3a3a3a; }
  .foot-brand { position: absolute; left: 608px; top: 68px; display: flex; align-items: center; gap: 5px; color: #cfcfcf; }
  .foot-brand .brand-name { color: #cfcfcf; font-size: 18px; }
  .foot-brand .brand-sub { color: #cfcfcf; border-color: #cfcfcf; }
  .social { position: absolute; top: 127px; width: 20px; height: 20px; border-radius: 50%; background: #1a6fc4; border: 1.5px solid var(--white); }
  .copyright { position: absolute; left: 0; top: 1167px; width: 802px; height: 33px; background: var(--blue); color: var(--white); font-size: 9px; display: flex; align-items: center; justify-content: center; }
</style>
</head>
<body>

<header class="site-header">
  <div class="brand">
    <span class="brand-name">HARLOW</span>
    <span class="brand-sub">REAL<br>ESTATE<br>MANAGEMENT</span>
  </div>
  <nav class="main-nav">
    <a class="active" style="left:349px">HOME</a>
    <a style="left:413px">ABOUT</a>
    <a style="left:482px">SERVICES</a>
    <a style="left:563px">CONTACT</a>
  </nav>
  <div class="call">
    <svg width="24" height="24" viewBox="0 0 24 24" fill="none" stroke="#0a3b85" stroke-width="2">
      <path d="M5 3 l4 0 l2 5 l-3 2 a11 11 0 0 0 6 6 l2 -3 l5 2 l0 4 a2 2 0 0 1 -2 2 A18 18 0 0 1 3 5 a2 2 0 0 1 2 -2z" fill="#0a3b85"/>
      <path d="M15 3 a7 7 0 0 1 6 6 M15 7 a3 3 0 0 1 2 2" stroke-linecap="round"/>
    </svg>
    <div class="call-text"><div class="label">CALL US</div><div class="num">(555)-210-4830</div></div>
  </div>
</header>

<section class="hero" role="img" aria-label="Photo of a modern city skyline with glass office towers at dusk">
  <svg class="hero-arrow" style="left:36px" width="14" height="26" viewBox="0 0 14 26"><path d="M12 1 L2 13 L12 25" stroke="#fff" stroke-width="2" fill="none"/></svg>
  <svg class="hero-arrow" style="left:752px" width="14" height="26" viewBox="0 0 14 26"><path d="M2 1 L12 13 L2 25" stroke="#fff" stroke-width="2" fill="none"/></svg>
  <h1 class="hero-title">PROVIDING QUALITY COMMERCIAL &amp; MULTIFAMILY PORTFOLIO<br>MANAGEMENT TO LANDLORDS, REITS, &amp; FINANCIAL INSTITUTIONS</h1>
  <div class="hero-btn">CONTACT NOW!</div>
</section>

<h2 class="welcome-title">WELCOME TO <span class="brand-inline">HARLOW</span></h2>
<div class="rule" style="left:250px;top:422px;width:302px"></div>
<p class="lead">Lorem ipsum dolor sit amet, consectetuer adipiscing elit, sed diam nonummy nibh euismod tincidun.</p>
<p class="intro">Lorem ipsum dolor sit amet, consectetuer adipiscing elit, sed diam nonummy nibh euismod tincidunt ut laoreet dolore magna aliquam erat volutpat. Ut wisi enim ad minim veniam, quis nostrud exerci tation ullamcorper suscipit lobortis nisl ut aliquip ex ea commodo consequat. Duis autem vel eum iriure dolor in hendrerit in vulputate velit esse molestie consequat, vel illum dolore eu feugiat nulla facilisis at vero eros et accumsan et iusto odio dignissim qui blandit praesent luptatum zzril delenit augue duis dolore te feugait nulla facilisi suscipit lobortis nisl ut aliquip ex ea commodo consequat.</p>
<div class="outline-btn">READ MORE</div>

<section class="services">
  <h2 class="services-title">OUR <span>SERVICES</span></h2>
  <div class="rule" style="left:312px;top:58px;width:178px"></div>

  <article class="card featured" style="left:54px">
    <div class="card-photo" role="img" aria-label="Photo of a bright open-plan office with desks and red chairs" style="background:linear-gradient(180deg,#e8e6e2,#c9c2b8 60%,#b08a6a)"></div>
    <div class="card-icon"><svg width="16" height="16" viewBox="0 0 16 16" fill="#fff"><circle cx="9" cy="3" r="2.2"/><rect x="6" y="6" width="6" height="5" rx="1"/><rect x="2" y="11" width="12" height="2"/></svg></div>
    <h3 class="card-title">MANAGE OFFICES</h3>
    <p class="card-text">Lorem ipsum dolor sit amet, consectetuer adipiscing elit, sed diam nonummy nibh euismod tincidunt ut laoreet dolore magna aliqua.</p>
    <div class="card-btn">READ MORE</div>
  </article>

  <article class="card" style="left:230px">
    <div class="card-photo" role="img" aria-label="Photo of a retail shop interior with shelves and counter" style="background:linear-gradient(180deg,#d9c9a8,#b8a07a 55%,#8a6f4f)"></div>
    <div class="card-icon"><svg width="16" height="16" viewBox="0 0 16 16" fill="none" stroke="#fff" stroke-width="1.5"><path d="M2 5 L3 2 H13 L14 5 Z" fill="#fff"/><rect x="3" y="6" width="10" height="8"/><rect x="6" y="9" width="4" height="5"/></svg></div>
    <h3 class="card-title">RETAIL</h3>
    <p class="card-text">Lorem ipsum dolor sit amet, consectetuer adipiscing elit, sed diam nonummy nibh euismod tincidunt ut laoreet dolore magna aliqua.</p>
    <div class="card-btn">READ MORE</div>
  </article>

  <article class="card" style="left:407px">
    <div class="card-photo" role="img" aria-label="Photo of a brick apartment building at a street corner" style="background:linear-gradient(180deg,#7fa6cf,#8a5a4a 50%,#5a4038)"></div>
    <div class="card-icon"><svg width="16" height="16" viewBox="0 0 16 16" fill="#fff"><rect x="3" y="3" width="7" height="11"/><rect x="10" y="6" width="4" height="8"/><rect x="5" y="5" width="1.5" height="1.5" fill="#3a3a3a"/><rect x="7" y="5" width="1.5" height="1.5" fill="#3a3a3a"/><rect x="5" y="8" width="1.5" height="1.5" fill="#3a3a3a"/><rect x="7" y="8" width="1.5" height="1.5" fill="#3a3a3a"/></svg></div>
    <h3 class="card-title">APARTMENTS</h3>
    <p class="card-text">Lorem ipsum dolor sit amet, consectetuer adipiscing elit, sed diam nonummy nibh euismod tincidunt ut laoreet dolore magna aliqua.</p>
    <div class="card-btn">READ MORE</div>
  </article>

  <article class="card" style="left:584px">
    <div class="card-photo" role="img" aria-label="Photo of a modern two-storey house lit at dusk" style="background:linear-gradient(180deg,#5e86b8,#8a8a86 55%,#4e4a3e)"></div>
    <div class="card-icon"><svg width="16" height="16" viewBox="0 0 16 16" fill="#fff"><path d="M1 8 L8 2 L15 8 Z"/><rect x="3" y="8" width="10" height="6"/><rect x="5" y="10" width="6" height="1" fill="#3a3a3a"/><rect x="5" y="12" width="6" height="1" fill="#3a3a3a"/></svg></div>
    <h3 class="card-title">OTHER PROPERTIES</h3>
    <p class="card-text">Lorem ipsum dolor sit amet, consectetuer adipiscing elit, sed diam nonummy nibh euismod tincidunt ut laoreet dolore magna aliqua.</p>
    <div class="card-btn">READ MORE</div>
  </article>
</section>

<footer class="site-footer">
  <h4 class="foot-title" style="left:53px">QUICK LINKS</h4>
  <div class="foot-rule" style="left:54px;width:89px"></div>
  <ul class="links"><li>Home</li><li>About</li><li>Services</li><li>Contact</li></ul>

  <h4 class="foot-title" style="left:186px">CONTACT DETAILS</h4>
  <div class="foot-rule" style="left:186px;width:167px"></div>
  <div class="contact-block"><strong>Harlow Real Estate Management</strong><br>48 Arbor Lane, Suite 5,<br>Fulton Road, NY - 104512</div>
  <div class="contact-row" style="top:114px"><svg width="9" height="9" viewBox="0 0 16 16" fill="#fff"><path d="M3 1 h3 l1.5 4 l-2 1.5 a9 9 0 0 0 4 4 l1.5 -2 l4 1.5 v3 a1.5 1.5 0 0 1 -1.5 1.5 A13 13 0 0 1 1.5 2.5 A1.5 1.5 0 0 1 3 1z"/></svg>555-210-4830</div>
  <div class="contact-row" style="top:139px"><svg width="10" height="9" viewBox="0 0 16 14" fill="#fff"><rect x="4" y="0" width="8" height="4"/><rect x="0" y="4" width="16" height="7" rx="1"/><rect x="4" y="9" width="8" height="5" fill="#fff" stroke="#252525"/></svg>555-210-4830</div>
  <div class="contact-row" style="top:164px"><svg width="10" height="8" viewBox="0 0 16 12"><rect x="0" y="0" width="16" height="12" fill="#fff"/><path d="M0 0 L8 7 L16 0" stroke="#252525" stroke-width="1.5" fill="none"/></svg>info@harlowrem.com</div>

  <div class="divider-v" style="left:372px"></div>

  <h4 class="foot-title" style="left:397px">QUICK&nbsp; INQUIRY</h4>
  <div class="foot-rule" style="left:397px;width:179px"></div>
  <div class="field" style="top:61px;height:23px">Name</div>
  <div class="field" style="top:90px;height:23px">Email</div>
  <div class="field" style="top:118px;height:29px">Message</div>
  <div class="submit">SUBMIT</div>

  <div class="divider-v" style="left:592px"></div>

  <div class="foot-brand"><span class="brand-name">HARLOW</span><span class="brand-sub">REAL<br>ESTATE<br>MANAGEMENT</span></div>
  <div class="social" style="left:650px" aria-label="Social link"></div>
  <div class="social" style="left:674px" aria-label="Social link"></div>
  <div class="social" style="left:697px" aria-label="Social link"></div>
</footer>
<div class="copyright">Copyright © 2017&nbsp; Harlow Real Estate Management. All Right Reserved</div>

</body>
</html>
```